Business Card Design for Flood Rescue 360 - Property Restoration Professionals

I need a business card designed for Flood Rescue 360. We are a full-service property restoration solution. Providing water, fire, smoke & storm restoration as well as mold remediation and full remodel or reconstruction to homes and businesses across Dallas-Fort Worth, TX.
Target Market(s)
home and business owners with insurance covered property damage from water, fire or storm related damage
Industry/Entity Type
property restoration
Contact Information for Business Card
Martin Kell General Manager Cell: 214-555-0193 Office: 469-555-0148 email: Martin@FloodRescue360.example services: Water, Fire, Mold, Reconstruction Tagline: Quick Help for Your Flood Crisis!
Look and feel
Each slider illustrates characteristics of the customer's brand and the style your logo design should communicate.

```html
<!DOCTYPE html>
<html lang="en">
<head>
<meta charset="utf-8">
<title>Flood Rescue 360 – Business Card</title>
<link href="https://fonts.googleapis.com/css2?family=Roboto:wght@400;500;700;900&display=swap" rel="stylesheet">
<style>
  :root {
    --stage: #121212;
    --brand-blue: #0fb3e6;
    --accent-blue: #19b2e4;
    --ink: #1b1b1b;
    --muted: #8a8a8a;
    --paper: #ffffff;
  }
  * { margin: 0; padding: 0; box-sizing: border-box; }
  html, body {
    width: 1200px; height: 960px; overflow: hidden;
    background: var(--stage);
    font-family: "Roboto", Arial, sans-serif;
  }
  .card {
    position: absolute; left: 249px; width: 702px; height: 401px;
    box-shadow: 0 14px 30px rgba(0,0,0,.55);
  }
  .card--front { top: 60px; background: var(--brand-blue); color: var(--paper); }
  .card--back { top: 500px; background: var(--paper); }

  .brand {
    position: absolute; display: flex; align-items: center; gap: 12px;
    font-weight: 900; line-height: 1; white-space: nowrap;
  }
  .brand__dot { border-radius: 50%; flex: none; }
  .card--front .brand { left: 0; right: 0; justify-content: center; top: 178px; font-size: 54px; color: var(--paper); }
  .card--front .brand__dot { width: 62px; height: 62px; border: 6px solid var(--paper); }

  .services { position: absolute; left: 0; right: 0; top: 335px; text-align: center; }
  .services__label {
    display: flex; align-items: center; justify-content: center; gap: 8px;
    font-size: 17px; font-weight: 500; letter-spacing: .5px;
  }
  .services__rule { width: 120px; height: 2px; background: var(--paper); opacity: .9; }
  .services__list {
    margin-top: 4px; display: flex; justify-content: center; gap: 8px;
    font-size: 17px; letter-spacing: .4px; list-style: none;
  }
  .services__list li { display: flex; align-items: center; gap: 6px; }
  .services__list li::before {
    content: ""; width: 10px; height: 10px; border-radius: 50%;
    border: 2px solid var(--paper);
  }

  .card--back .brand { left: 25px; top: 178px; font-size: 30px; color: var(--accent-blue); gap: 10px; }
  .card--back .brand__dot { width: 40px; height: 40px; border: 5px solid var(--accent-blue); }

  .divider { position: absolute; left: 350px; top: 80px; width: 1px; height: 241px; background: var(--accent-blue); }

  .contact { position: absolute; left: 382px; top: 124px; }
  .contact__name { font-size: 34px; font-weight: 700; line-height: 1; color: var(--accent-blue); }
  .contact__name .surname { font-weight: 400; color: var(--muted); }
  .contact__role { margin-top: 4px; font-size: 17px; color: var(--ink); letter-spacing: .3px; }
  .contact__list { list-style: none; margin-top: 22px; }
  .contact__list li {
    display: flex; align-items: center; gap: 11px;
    font-size: 17px; line-height: 23.5px; color: var(--ink); letter-spacing: .5px;
  }
  .contact__list svg { width: 15px; height: 15px; flex: none; }

  .tagline {
    position: absolute; left: 0; right: 0; top: 354px; text-align: center;
    font-size: 18px; color: var(--accent-blue); letter-spacing: .4px;
  }
</style>
</head>
<body>
  <section class="card card--front" aria-label="Card front">
    <div class="brand"><span class="brand__dot"></span>Flood Rescue 360</div>
    <div class="services">
      <div class="services__label"><span class="services__rule"></span>SERVICES<span class="services__rule"></span></div>
      <ul class="services__list">
        <li>Water</li><li>Fire</li><li>Mold</li><li>Reconstruction</li>
      </ul>
    </div>
  </section>

  <section class="card card--back" aria-label="Card back">
    <div class="brand"><span class="brand__dot"></span>Flood Rescue 360</div>
    <div class="divider"></div>
    <div class="contact">
      <h1 class="contact__name">Martin <span class="surname">Kell</span></h1>
      <p class="contact__role">General Manager</p>
      <ul class="contact__list">
        <li>
          <svg viewBox="0 0 16 16" aria-hidden="true"><rect x="4" y="1" width="8" height="14" rx="1.5" fill="none" stroke="#19b2e4" stroke-width="1.6"/></svg>
          214-555-0193
        </li>
        <li>
          <svg viewBox="0 0 16 16" aria-hidden="true"><path d="M3 2l3 0 1 3-2 1.5c1 2 2.5 3.5 4.5 4.5L11 9l3 1v3c0 .6-.4 1-1 1C7 14 2 9 2 3c0-.6.4-1 1-1z" fill="#19b2e4"/></svg>
          469-555-0148
        </li>
        <li>
          <svg viewBox="0 0 16 16" aria-hidden="true"><rect x="1" y="4" width="14" height="10" fill="none" stroke="#19b2e4" stroke-width="1.5"/><path d="M1 4l7 6 7-6" fill="none" stroke="#19b2e4" stroke-width="1.5"/></svg>
          Martin@FloodRescue360.example
        </li>
      </ul>
    </div>
    <p class="tagline">Quick Help for Your Flood Crisis!</p>
  </section>
</body>
</html>
```